4 page website for our new business,
www.Velna Crest Bathrooms.example
We will provide the follwing service
1st Home page, bathroom renvovations, make over redesign etc
2nd page Tiling service
3rd page Waterproofing
4th page Galllery
The home will maily focus on the core business bathroom renovation, customer should able request quote, via entering thier info eg. name and contact number and select the 3 services
Need area for testimonials that will scroll
Maybe a banner which may flash varies pic of different design
Maybe a area for giving reasons why customer should go with us for they job
simple site which will grentrate leads, create presece, build brand.
We've just had the logo design, which allow you to create theme.
Target Market(s)
home owner's mum and dad
Look and feel
Each slider illustrates characteristics of the customer's brand and the style your logo design should communicate.

```html
<!DOCTYPE html>
<html lang="en">
<head>
<meta charset="utf-8">
<title>Velna Crest Bathrooms</title>
<link rel="stylesheet" href="https://fonts.googleapis.com/css2?family=PT+Sans+Narrow:wght@400;700&display=swap">
<style>
:root{
  --ink:#ffffff;
  --steel:#4d8099;
  --steel-dark:#3f7088;
  --steel-light:#5f97b5;
  --panel-top:#5a93b2;
  --panel-bottom:#3e6f88;
  --header-top:#f4f4f4;
  --header-bottom:#e2e2e2;
  --sky-top:#f1f9fd;
  --sky-bottom:#b3dff4;
  --banner-dark:#5a5a5a;
  --banner-mid:#8a8a8a;
  --field:#f3f3f3;
  --footer-text:#4a4a4a;
  --muted:#6b6b6b;
}
*{margin:0;padding:0;box-sizing:border-box}
html,body{width:1029px;height:1200px;overflow:hidden}
body{
  position:relative;
  font-family:"PT Sans Narrow",sans-serif;
  background:linear-gradient(var(--sky-top) 0%,var(--sky-bottom) 92%);
  color:var(--ink);
}
.site-header{
  position:absolute;left:0;top:0;width:1029px;height:126px;
  background:linear-gradient(var(--header-top),var(--header-bottom));
  border-bottom:3px solid var(--steel);
}
.brand{
  position:absolute;left:62px;top:46px;display:flex;align-items:center;gap:12px;
  font-size:24px;font-weight:700;color:var(--steel);letter-spacing:.5px;
}
.brand-mark{width:22px;height:22px;background:var(--steel)}
.social{position:absolute;top:22px;left:904px;display:flex;gap:12px}
.social span{width:24px;height:24px;border-radius:4px;background:var(--steel-light)}
.main-nav{
  position:absolute;left:540px;top:92px;width:440px;height:34px;
  background:var(--steel);display:flex;
}
.main-nav a{
  color:var(--ink);text-decoration:none;font-size:15px;line-height:34px;
  padding:0 0 0 14px;flex:none;
}
.main-nav a.current{
  background:var(--steel-light);width:59px;padding:0;text-align:center;
  margin-top:-6px;line-height:40px;height:40px;position:relative;
}
.main-nav a.current::after{
  content:"";position:absolute;left:24px;bottom:0;border:6px solid transparent;border-bottom:0;border-top-color:#fff;
}
.nav-item{width:96px}
.banner{
  position:absolute;left:0;top:160px;width:1029px;height:193px;
  background:linear-gradient(var(--banner-mid),var(--banner-dark));
}
.banner-photo{
  position:absolute;left:0;top:0;width:637px;height:193px;
  background:linear-gradient(100deg,#8f8f8f 0%,#d9dadb 30%,#f2f3f3 55%,#cfd0d0 100%);
}
.slide-arrow{position:absolute;top:86px;width:20px;height:20px}
.quick-note{
  position:absolute;left:637px;top:149px;width:325px;height:213px;
  background:linear-gradient(var(--panel-top),var(--steel-dark));
  padding:18px 16px;
}
.quick-note h2{font-size:15px;font-weight:400;display:flex;align-items:center;gap:8px;margin-bottom:14px}
.field-row{display:flex;justify-content:flex-end;align-items:center;gap:10px;margin-bottom:18px;font-size:15px}
.field-row .field{width:201px;height:19px;background:var(--field);border:1px solid #d6d6d6;position:relative}
.field.select::after{content:"";position:absolute;right:1px;top:1px;width:15px;height:15px;background:#c7d6ea}
.field-row label{text-align:right}
.field-row.wide{justify-content:space-between}
.submit{
  position:absolute;right:20px;bottom:22px;width:85px;height:23px;border-radius:6px;
  background:linear-gradient(#fafafa,#dcdcdc);color:#5d5d5d;font-size:14px;
  display:flex;align-items:center;justify-content:center;gap:8px;
}
.services{
  position:absolute;left:50px;top:379px;width:929px;height:370px;display:flex;
  background:linear-gradient(var(--panel-top),var(--panel-bottom));
  box-shadow:0 14px 14px -10px rgba(60,100,120,.25);
}
.service{flex:1;padding:12px 16px;position:relative;border-left:1px solid #c9dde8}
.service:first-child{border-left:0}
.panel-title{font-size:15px;font-weight:700;display:flex;align-items:center;gap:14px}
.service-photo{
  margin:10px auto 0;width:234px;height:157px;border:2px solid #fff;
}
.service p{font-size:12.5px;line-height:19.6px;margin-top:32px;padding-right:4px}
.read-more{
  position:absolute;right:16px;bottom:8px;font-size:12.5px;display:flex;align-items:center;gap:6px;
}
.lower{
  position:absolute;left:50px;top:777px;width:929px;height:272px;
  background:linear-gradient(var(--panel-top),var(--panel-bottom));
  box-shadow:0 14px 14px -10px rgba(60,100,120,.25);
}
.testimonials{position:absolute;left:0;top:0;width:418px;height:272px;padding:10px 16px;border-right:1px solid rgba(255,255,255,.15)}
.testimonial{position:relative;height:100px;margin-top:22px}
.testimonial + .testimonial{margin-top:2px}
.thumb{position:absolute;left:0;top:2px;width:88px;height:59px;border:2px solid #fff}
.testimonial h3{position:absolute;left:105px;top:0;font-size:15px;font-weight:400;color:#2f3e47}
.testimonial p{position:absolute;left:105px;top:24px;width:290px;font-size:12.5px;line-height:19.6px}
.testimonial .read-more{right:22px;bottom:auto;top:68px}
.gallery{position:absolute;left:430px;top:0;width:499px;height:272px;padding:10px 17px}
.gallery-strip{
  position:absolute;left:17px;top:78px;width:466px;height:115px;border-radius:8px;background:#f2f2f2;
}
.gallery-photo{position:absolute;top:17px;width:117px;height:79px;border:2px solid #fff;box-shadow:0 4px 5px rgba(0,0,0,.2)}
.strip-arrow{position:absolute;top:50px}
.site-footer{
  position:absolute;left:0;top:1104px;width:1029px;height:96px;
  background:linear-gradient(#f7f7f7,#e6e6e6);border-top:1px solid #d4d4d4;text-align:center;
}
.footer-nav{display:flex;justify-content:center;gap:0;margin-top:24px;padding-left:4px}
.footer-nav a{color:var(--footer-text);text-decoration:none;font-size:14.5px;padding:0 19px}
.copyright{font-size:10.5px;color:var(--muted);margin-top:7px;padding-left:10px}
</style>
</head>
<body>
<header class="site-header">
  <div class="brand"><span class="brand-mark"></span>VELNA CREST BATHROOMS</div>
  <div class="social"><span aria-label="Social profile one"></span><span aria-label="Social profile two"></span></div>
  <nav class="main-nav">
    <a class="current" href="#">Home</a>
    <a class="nav-item" href="#" style="width:94px;padding-left:34px">About us</a>
    <a class="nav-item" href="#" style="width:82px;padding-left:14px">Services</a>
    <a class="nav-item" href="#" style="width:104px;padding-left:10px">Quick Quote</a>
    <a class="nav-item" href="#" style="width:101px;padding-left:26px">Contact us</a>
  </nav>
</header>

<section class="banner">
  <div class="banner-photo" role="img" aria-label="Bright white bathroom with freestanding tub, wall-hung toilet and basin by a large window"></div>
  <svg class="slide-arrow" style="left:62px" viewBox="0 0 20 20"><circle cx="10" cy="10" r="8.5" fill="none" stroke="#fff" stroke-width="2"/><path d="M12 5.5 7 10l5 4.5z" fill="#fff"/></svg>
  <svg class="slide-arrow" style="left:600px" viewBox="0 0 20 20"><circle cx="10" cy="10" r="8.5" fill="none" stroke="#fff" stroke-width="2"/><path d="M8 5.5 13 10l-5 4.5z" fill="#fff"/></svg>
</section>

<form class="quick-note">
  <h2><svg width="24" height="20" viewBox="0 0 24 20"><path d="M3 6c2-4 12-5 16 0 3 4-1 9-7 9l-4 4 1-5C3 12 1 9 3 6z" fill="#fff"/></svg>Quick note</h2>
  <div class="field-row"><label>Name</label><span class="field"></span></div>
  <div class="field-row"><label>Number</label><span class="field"></span></div>
  <div class="field-row wide"><label>Services needed</label><span class="field select"></span></div>
  <div class="submit">Submit <svg width="15" height="15" viewBox="0 0 20 20"><circle cx="10" cy="10" r="8.5" fill="none" stroke="#4d8099" stroke-width="2"/><path d="M8 5.5 13 10l-5 4.5z" fill="#4d8099"/></svg></div>
</form>

<section class="services">
  <article class="service">
    <h2 class="panel-title">Bathroom Renovations <svg width="24" height="14" viewBox="0 0 24 14"><path d="M1 1l6 6-6 6h5l6-6-6-6zM11 1l6 6-6 6h5l6-6-6-6z" fill="#fff"/></svg></h2>
    <div class="service-photo" role="img" aria-label="Renovated bathroom with timber vanity, bathtub and glass shower" style="background:linear-gradient(160deg,#d8dde0,#a08a72 60%,#7a6652)"></div>
    <p>Lorem Ipsum is simply dummy text of the printing and type-setting industry. Lorem Ipsum has been the industry's standard dummy text ever since the 1500s, when an unknown printer took a galley of type and scrambled it to make a type specimen book</p>
    <span class="read-more">Read more <svg width="13" height="13" viewBox="0 0 20 20"><circle cx="10" cy="10" r="8.5" fill="none" stroke="#fff" stroke-width="2"/><path d="M8 5.5 13 10l-5 4.5z" fill="#fff"/></svg></span>
  </article>
  <article class="service">
    <h2 class="panel-title">Tiling Services <svg width="24" height="14" viewBox="0 0 24 14"><path d="M1 1l6 6-6 6h5l6-6-6-6zM11 1l6 6-6 6h5l6-6-6-6z" fill="#fff"/></svg></h2>
    <div class="service-photo" role="img" aria-label="Cream marble-tiled bathroom with built-in bathtub" style="background:linear-gradient(#c9c0b4,#e6ddd1 50%,#d4c6b3);width:246px;height:162px"></div>
    <p style="margin-top:27px">Lorem Ipsum is simply dummy text of the printing and type-setting industry. Lorem Ipsum has been the industry's standard dummy text ever since the 1500s, when an unknown printer took a galley of type and scrambled it to make a type specimen book</p>
    <span class="read-more">Read more <svg width="13" height="13" viewBox="0 0 20 20"><circle cx="10" cy="10" r="8.5" fill="none" stroke="#fff" stroke-width="2"/><path d="M8 5.5 13 10l-5 4.5z" fill="#fff"/></svg></span>
  </article>
  <article class="service">
    <h2 class="panel-title">Waterproofing <svg width="24" height="14" viewBox="0 0 24 14"><path d="M1 1l6 6-6 6h5l6-6-6-6zM11 1l6 6-6 6h5l6-6-6-6z" fill="#fff"/></svg></h2>
    <div class="service-photo" role="img" aria-label="Dark-tiled bathroom with white freestanding bath and glass screen" style="background:linear-gradient(#2f2f33,#6d6d70 50%,#3a3a3d);width:234px;height:161px"></div>
    <p style="margin-top:28px">Lorem Ipsum is simply dummy text of the printing and type-setting industry. Lorem Ipsum has been the industry's standard dummy text ever since the 1500s, when an unknown printer took a galley of type and scrambled it to make a type specimen book</p>
    <span class="read-more">Read more <svg width="13" height="13" viewBox="0 0 20 20"><circle cx="10" cy="10" r="8.5" fill="none" stroke="#fff" stroke-width="2"/><path d="M8 5.5 13 10l-5 4.5z" fill="#fff"/></svg></span>
  </article>
</section>

<section class="lower">
  <div class="testimonials">
    <h2 class="panel-title">Testimonals <svg width="24" height="14" viewBox="0 0 24 14"><path d="M1 1l6 6-6 6h5l6-6-6-6zM11 1l6 6-6 6h5l6-6-6-6z" fill="#fff"/></svg></h2>
    <div class="testimonial">
      <div class="thumb" role="img" aria-label="Customer's renovated bathroom" style="background:linear-gradient(160deg,#d8dde0,#a08a72 60%,#7a6652)"></div>
      <h3>Testimonals 01</h3>
      <p>Lorem Ipsum is simply dummy text of the printing and type-setting industry. Lorem Ipsum</p>
      <span class="read-more">Read more <svg width="13" height="13" viewBox="0 0 20 20"><circle cx="10" cy="10" r="8.5" fill="none" stroke="#fff" stroke-width="2"/><path d="M8 5.5 13 10l-5 4.5z" fill="#fff"/></svg></span>
    </div>
    <div class="testimonial">
      <div class="thumb" role="img" aria-label="Customer's renovated bathroom" style="background:linear-gradient(160deg,#d8dde0,#a08a72 60%,#7a6652)"></div>
      <h3>Testimonals 01</h3>
      <p>Lorem Ipsum is simply dummy text of the printing and type-setting industry. Lorem Ipsum</p>
      <span class="read-more">Read more <svg width="13" height="13" viewBox="0 0 20 20"><circle cx="10" cy="10" r="8.5" fill="none" stroke="#fff" stroke-width="2"/><path d="M8 5.5 13 10l-5 4.5z" fill="#fff"/></svg></span>
    </div>
  </div>
  <div class="gallery">
    <h2 class="panel-title">Photogallery <svg width="24" height="14" viewBox="0 0 24 14"><path d="M1 1l6 6-6 6h5l6-6-6-6zM11 1l6 6-6 6h5l6-6-6-6z" fill="#fff"/></svg></h2>
    <div class="gallery-strip">
      <svg class="strip-arrow" style="left:9px" width="12" height="14" viewBox="0 0 12 14"><path d="M1 1h4l6 6-6 6H1l6-6z" fill="#666"/></svg>
      <div class="gallery-photo" style="left:30px;background:linear-gradient(#c9c0b4,#e6ddd1 50%,#d4c6b3)" role="img" aria-label="Marble-tiled bathroom"></div>
      <div class="gallery-photo" style="left:178px;background:linear-gradient(#2f2f33,#6d6d70 50%,#3a3a3d)" role="img" aria-label="Dark-tiled bathroom with freestanding bath"></div>
      <div class="gallery-photo" style="left:320px;background:linear-gradient(160deg,#d8dde0,#a08a72 60%,#7a6652)" role="img" aria-label="Bathroom with timber vanity"></div>
      <svg class="strip-arrow" style="left:445px" width="12" height="14" viewBox="0 0 12 14"><path d="M11 1H7L1 7l6 6h4L5 7z" fill="#666"/></svg>
    </div>
  </div>
</section>

<footer class="site-footer">
  <nav class="footer-nav">
    <a href="#">Home</a><a href="#">About us</a><a href="#">Services</a><a href="#">Quick Quote</a><a href="#">Contact us</a>
  </nav>
  <p class="copyright">© copyrights velnacrestbathrooms.example.All rights reserved</p>
</footer>
</body>
</html>
```